Flyer for spiritual retreat (yoga, meditation, reiki, raw food)

I would like a flyer to promote my upcoming retreat and a matching Facebook banner.

The name of the retreat is "Wavecrest Of Calm" and the tagline is "retreat into you"

The activities in the retreat include daily meditation, ecstatic dance, spiritual development workshops on intuition, energy healing etc and a reiki session is included.

I would like a flyer designed to promote this, something that is editable as I will be running this multiple times and will need to adjust the flyer to add the dates etc each time.

edit: add that here will be fully catered raw food and juices, and that the retreat price includes all accomodation, meals and workshops.

Please contact me if you need further info. Please also visit my website www.marithovland.com and www.facebook.com/tolvanahaven to see my current events and promotions.

Thank you,

Marit

Reason: Hi all, thank you all for your submissions. Apologies as I am traveling and do not have much access to internet and will review your submissions and provide feedback as soon as possible. Kind regards, Marit.

Target Market(s)

People who like meditation, yoga, fans of rowan mabry and jasper vinek, those interested in personal and spiritual development.

Industry/Entity Type

Health And Wellness

Requirements
Must have
• Please put the included reiki session as as added bonus. Something like "BONUS 30 minute reiki healing session" in a little star/banner/something that stands out.
• Please emphasise the "light" part of Wavecrest as I am going for a play on words between in the light and enlightenment.
• Please include placeholder text for place, location, time
• Placeholder for price
• My name (see attached file - can change colour to suit) and website (www.marithovland.com)
Nice to have
• I prefer rounded designs, curves rather than block designs.
Should not have
• Tolvana Haven logo

```html
<!DOCTYPE html>
<html lang="en">
<head>
<meta charset="utf-8">
<title>Wavecrest Of Calm – Facebook Cover</title>
<link rel="stylesheet" href="https://fonts.googleapis.com/css2?family=Bungee+Inline&family=Oswald:wght@300;400;500&family=Archivo+Black&display=swap">
<style>
  :root {
    --teal: #14a3b4;
    --lime: #a8c21a;
    --yellow: #e6d31a;
    --gold: #d9b84a;
    --ink: #050a08;
    --deep-green: #0b3a2a;
    --paper: #ffffff;
  }
  * { margin: 0; padding: 0; box-sizing: border-box; }
  html, body { width: 1200px; height: 1200px; overflow: hidden; background: var(--paper); }
  .board { position: relative; width: 1200px; height: 1200px; }

  .board-title {
    position: absolute; top: 248px; left: 0; width: 100%;
    text-align: center; font-family: "Bungee Inline", sans-serif;
    font-size: 86px; letter-spacing: 10px; color: var(--teal);
  }

  .cover {
    position: absolute; left: 42px; top: 390px; width: 1117px; height: 419px;
    overflow: hidden; background: var(--ink);
    box-shadow: 14px 16px 14px rgba(0,0,0,.55);
  }

  .hero-art {
    position: absolute; left: 0; top: 0; width: 760px; height: 100%;
    background:
      radial-gradient(ellipse at 18% 30%, #3fe6e0 0%, #0f8f8c 28%, transparent 55%),
      radial-gradient(ellipse at 55% 40%, #1fae5a 0%, #0b5a3a 35%, transparent 65%),
      radial-gradient(ellipse at 15% 85%, #6fc7b4 0%, #2a6e6a 30%, transparent 55%),
      linear-gradient(90deg, #0a4a4a 0%, #063a2e 60%, var(--ink) 100%);
  }
  .glow-art {
    position: absolute; right: 0; top: 0; width: 380px; height: 100%;
    background:
      radial-gradient(ellipse at 20% 0%, #e8e23a 0%, #7a7a10 18%, transparent 40%),
      linear-gradient(180deg, #050805 0%, #0b1a0a 45%, #0f5a34 100%);
  }

  .owner-name {
    position: absolute; left: 96px; top: 160px;
    font-family: "Oswald", sans-serif; font-weight: 400;
    font-size: 26px; color: var(--gold);
  }
  .owner-site {
    position: absolute; left: 142px; top: 226px;
    font-family: "Oswald", sans-serif; font-size: 11px; letter-spacing: .5px;
    color: #e8f4f0;
  }

  .bonus-word {
    position: absolute; left: 490px; top: 8px;
    writing-mode: vertical-rl;
    font-family: "Oswald", sans-serif; font-weight: 500;
    font-size: 66px; line-height: 1; letter-spacing: -1px; color: var(--teal);
  }
  .bonus-number {
    position: absolute; left: 562px; top: -30px;
    font-family: "Oswald", sans-serif; font-weight: 300;
    font-size: 240px; line-height: 1; letter-spacing: -8px; color: var(--lime);
  }
  .bonus-unit {
    position: absolute; left: 560px; top: 204px;
    font-family: "Oswald", sans-serif; font-weight: 300;
    font-size: 64px; line-height: 1; color: var(--teal);
  }

  .reiki-ribbon {
    position: absolute; left: 450px; top: 268px; width: 350px; height: 64px;
    border-top: 2px solid var(--lime); border-bottom: 2px solid var(--lime);
    background: rgba(168,194,26,.12);
    display: flex; align-items: center; justify-content: center;
  }
  .reiki-ribbon::before, .reiki-ribbon::after {
    content: ""; position: absolute; top: 22px; width: 16px; height: 16px;
    border: 2px solid var(--lime); transform: rotate(45deg);
  }
  .reiki-ribbon::before { left: -26px; }
  .reiki-ribbon::after { right: -26px; }
  .reiki-label {
    font-family: "Oswald", sans-serif; font-size: 26px;
    font-variant: small-caps; letter-spacing: 1px; color: var(--lime);
  }

  .catering-note {
    position: absolute; left: 428px; top: 352px; width: 400px;
    font-family: "Oswald", sans-serif; font-size: 16px; line-height: 28px;
    text-transform: uppercase; color: var(--yellow); text-align: center;
  }

  .retreat-info {
    position: absolute; right: 7px; top: 20px; width: 360px; text-align: right;
  }
  .retreat-name {
    font-family: "Archivo Black", sans-serif; font-size: 52px; line-height: 1;
    color: #111; -webkit-text-stroke: 1px #cfcfa0; letter-spacing: -1px;
  }
  .retreat-sub {
    font-family: "Oswald", sans-serif; font-size: 42px; line-height: 46px;
    font-variant: small-caps; color: var(--yellow); margin-top: 4px;
  }
  .tagline {
    font-family: "Oswald", sans-serif; font-size: 36px; line-height: 40px;
    font-variant: small-caps; color: var(--lime);
  }
  .activities {
    font-family: "Archivo Black", sans-serif; font-size: 13.5px; line-height: 17.6px;
    color: var(--yellow); margin-top: 4px;
  }
  .details {
    font-family: "Archivo Black", sans-serif; font-size: 24px; line-height: 24px;
    color: var(--teal); margin-top: 8px; text-transform: uppercase;
  }
  .price {
    font-family: "Oswald", sans-serif; font-size: 44px; line-height: 48px;
    color: var(--lime);
  }
</style>
</head>
<body>
<div class="board">
  <h1 class="board-title">FB Cover Photo</h1>

  <section class="cover">
    <div class="hero-art" role="img" aria-label="Silhouette of a woman in a yoga pose over glowing teal and green light swirls, with a bowl of polished healing crystals in the corner"></div>
    <div class="glow-art" role="img" aria-label="Yellow rays of light glowing above a dark green candle-lit background"></div>

    <p class="owner-name">Marit Hovland</p>
    <p class="owner-site">WWW.MARITHOVLAND.COM</p>

    <span class="bonus-word">BONUS</span>
    <span class="bonus-number">30</span>
    <span class="bonus-unit">MINUTES</span>

    <div class="reiki-ribbon"><span class="reiki-label">Reiki Healing Session</span></div>

    <p class="catering-note">Fully catered raw food and juices, retreat price includes all accomodation, meals and workshops.</p>

    <div class="retreat-info">
      <h2 class="retreat-name">WaveCREST</h2>
      <p class="retreat-sub">Of Calm</p>
      <p class="tagline">Retreat Into You</p>
      <p class="activities">The activities in the retreat<br>include daily meditation,<br>ecstatic dance, spiritual<br>development workshops<br>on intuition, energy<br>healing etc. and a reiki<br>session is included.</p>
      <p class="details">Place<br>Location<br>Time</p>
      <p class="price">$00.00</p>
    </div>
  </section>
</div>
</body>
</html>
```